Corporate Dinner Invite at Corvessa for Halvern

Halvern is hosting a corporate dinner at the PRV Summit and we need an email attachment invite for the event. Please use some images from this site for inspiration: https://www.corvessachicago.com/ivyparlor/

Invite Title:
Join us for dinner!

Event Details:
Tuesday, October 24th 2023 at 6:30pm
Corvessa Chicago, Ivy Parlor
437 W Larkmoor Ave, Chicago, IL 60614

Target Market(s)

Corporate Audience

Font styles to use
Script

Colors
0054AA
0677BA
7BADD7
CADEEF
E8F1F8

Requirements
Must have
• Halvern logo, event date / time, event location details, photo(s) from Ivy Parlor

```html
<!DOCTYPE html>
<html lang="en">
<head>
<meta charset="utf-8">
<title>Join Us for Dinner – Halvern at Corvessa Chicago</title>
<link rel="stylesheet" href="https://fonts.googleapis.com/css2?family=Cinzel:wght@600;700;800&family=Cormorant+Garamond:wght@500;600&display=swap">
<style>
  :root {
    --bg: #1a1a1b;
    --bg-light: #242426;
    --white: #ffffff;
    --accent: #3f82f0;
    --accent-deep: #1a3fa8;
    --label: #3f7ff0;
    --brand: #2a6fe0;
    --photo-yellow: #d6dc5a;
    --photo-purple: #6a2d8c;
    --photo-wood: #3a2612;
  }
  * { margin: 0; padding: 0; box-sizing: border-box; }
  html, body { width: 1200px; height: 797px; overflow: hidden; background: var(--bg); }
  .invite {
    position: relative;
    width: 1200px;
    height: 797px;
    overflow: hidden;
    background: radial-gradient(ellipse at 75% 40%, var(--bg-light) 0%, var(--bg) 70%);
    font-family: "Cormorant Garamond", Georgia, serif;
    color: var(--white);
  }
  .venue-photo {
    position: absolute;
    left: 0; top: 0;
    width: 560px; height: 797px;
    background:
      radial-gradient(circle at 28% 22%, var(--photo-yellow) 0%, rgba(214,220,90,0.35) 12%, transparent 30%),
      radial-gradient(ellipse at 30% 30%, rgba(127,143,42,0.8) 0%, transparent 55%),
      radial-gradient(ellipse at 55% 62%, var(--photo-purple) 0%, transparent 40%),
      linear-gradient(to bottom, #0f1408 0%, #20280c 40%, #2b1d36 62%, var(--photo-wood) 82%, #1a1008 100%);
  }
  .venue-photo::after {
    content: "";
    position: absolute;
    inset: 0;
    background: linear-gradient(to right, transparent 0%, transparent 60%, rgba(26,26,27,0.7) 85%, var(--bg) 100%);
  }
  .brand {
    position: absolute;
    left: 980px; top: 82px;
    display: flex; align-items: center; gap: 8px;
    font-family: "Cinzel", Georgia, serif;
    font-weight: 700;
    font-size: 26px;
    color: var(--brand);
  }
  .brand-mark { width: 16px; height: 16px; background: var(--brand); }
  .headline {
    position: absolute;
    left: 522px; top: 126px;
    font-family: "Cinzel", Georgia, serif;
    font-weight: 800;
    line-height: 1;
  }
  .headline-top { display: block; font-size: 74px; color: var(--white); letter-spacing: -1px; }
  .headline-bottom { display: block; font-size: 76px; color: var(--accent); margin-top: 4px; letter-spacing: -1px; }
  .details-button {
    position: absolute;
    left: 526px; top: 336px;
    width: 429px; height: 103px;
    background: var(--accent);
    border: 4px solid var(--accent-deep);
    display: flex; align-items: center; justify-content: center;
    font-family: "Cinzel", Georgia, serif;
    font-weight: 700;
    font-size: 40px;
    color: var(--white);
    letter-spacing: -0.5px;
  }
  .detail-row {
    position: absolute;
    left: 537px;
    display: flex; align-items: center;
  }
  .detail-label {
    width: 127px; height: 41px;
    border: 2px solid var(--accent-deep);
    display: flex; align-items: center; justify-content: center;
    font-family: "Cinzel", Georgia, serif;
    font-weight: 700;
    font-size: 20px;
    letter-spacing: 2px;
    color: var(--label);
  }
  .detail-value {
    margin-left: 35px;
    font-size: 23px;
    font-weight: 500;
    letter-spacing: 0.4px;
    text-transform: uppercase;
    font-variant-numeric: lining-nums;
    white-space: nowrap;
    line-height: 1.1;
  }
  .row-venue .detail-value { margin-left: 30px; font-size: 22px; letter-spacing: 0.2px; }
  .row-date { top: 499px; }
  .row-time { top: 579px; }
  .row-venue { top: 658px; }
</style>
</head>
<body>
  <main class="invite">
    <div class="venue-photo" role="img" aria-label="Cocktails on a bar table at Ivy Parlor with warm bokeh lights"></div>

    <div class="brand"><span class="brand-mark"></span>HALVERN</div>

    <h1 class="headline">
      <span class="headline-top">JOIN US</span>
      <span class="headline-bottom">FOR DINNER!</span>
    </h1>

    <div class="details-button">EVENT DETAILS</div>

    <div class="detail-row row-date">
      <div class="detail-label">DATE</div>
      <div class="detail-value">Tuesday, October 24th 2023</div>
    </div>
    <div class="detail-row row-time">
      <div class="detail-label">TIME</div>
      <div class="detail-value">6:30PM</div>
    </div>
    <div class="detail-row row-venue">
      <div class="detail-label">VENUE</div>
      <div class="detail-value">Corvessa Chicago, Ivy Parlor<br>437 W Larkmoor Ave, Chicago, IL 60614</div>
    </div>
  </main>
</body>
</html>
```